Letterhead Design Project

Looking for letterhead designs for Dravesco Mining.

I am looking for a letterhead design in conjunction with a business card design. I have opened contests for both but ask that if you submit a letterhead design you also submit a business card design with a corresponding look/feel.

Dravesco Mining is a B2B company that buys and sells large machinery tires within the coal mining industry. The design should the strong, crisp and masculine. I have uploaded the company logo and mock-up of the back of the company's business card.

Color scheme should be grey/green/black

Contact information to include:
Name: Tom Sealbrook
Title: Managing Director
Phone: 555-314-2097
Address: 1186 Pelham #3 Dallas, TX 75209
Email: Tom@Dravesco.example

Project Deadline Extended
Reason: Looking for a more refined, elegant letterhead than what's been submitted as of yet. Here is a sample of what we're looking for: http://www.plumbridgestudio.example/letterhead-designs/ We will also be increasing the payment.

```html
<!DOCTYPE html>
<html lang="en">
<head>
<meta charset="utf-8">
<title>Dravesco Mining — Letterhead</title>
<link href="https://fonts.googleapis.com/css2?family=Questrial&display=swap" rel="stylesheet">
<style>
  :root {
    --backdrop: #efefef;
    --paper: #fbfbfb;
    --charcoal: #5b5c5e;
    --ink: #58595b;
    --green: #4fa01e;
    --band-grey: #dedede;
    --mark-white: #ececec;
  }
  html, body {
    margin: 0;
    width: 1200px;
    height: 815px;
    overflow: hidden;
    background: var(--backdrop);
    font-family: "Questrial", "Century Gothic", sans-serif;
  }
  .sheet {
    position: absolute;
    top: 70px;
    width: 482px;
    height: 684px;
    box-sizing: border-box;
  }
  .letterhead { left: 80px; background: var(--paper); }
  .back-cover { left: 638px; background: var(--charcoal); }

  .wordmark {
    position: absolute;
    left: 38px;
    top: 42px;
    display: flex;
    align-items: center;
    gap: 8px;
  }
  .wordmark-square {
    width: 14px;
    height: 14px;
    background: var(--green);
  }
  .wordmark-name {
    font-size: 21px;
    color: var(--ink);
    letter-spacing: 0.5px;
    white-space: nowrap;
  }

  .contact {
    position: absolute;
    left: 38px;
    top: 100px;
    font-size: 7.5px;
    line-height: 9px;
    color: var(--ink);
  }
  .contact p { margin: 0; }
  .contact-name { text-transform: uppercase; letter-spacing: 0.3px; }
  .contact-title { color: var(--green); margin-bottom: 5px; }
  .contact-label { color: var(--green); }

  .side-band {
    position: absolute;
    bottom: 0;
    background: var(--band-grey);
  }
  .side-band-left { left: 0; width: 30px; height: 174px; }
  .side-band-right { right: 0; width: 40px; height: 398px; }

  .cover-mark {
    position: absolute;
    left: 0;
    right: 0;
    top: 326px;
    display: flex;
    justify-content: center;
    align-items: center;
    gap: 12px;
  }
  .cover-mark-square {
    width: 22px;
    height: 22px;
    background: var(--green);
  }
  .cover-mark-name {
    font-size: 30px;
    color: var(--mark-white);
    letter-spacing: 1px;
  }
</style>
</head>
<body>
  <section class="sheet letterhead">
    <div class="wordmark">
      <span class="wordmark-square"></span>
      <span class="wordmark-name">DRAVESCO MINING</span>
    </div>

    <div class="contact">
      <p class="contact-name">Tom Sealbrook</p>
      <p class="contact-title">Managing Director</p>
      <p><span class="contact-label">T:</span> 555-314-2097</p>
      <p><span class="contact-label">E:</span> Tom@Dravesco.example</p>
      <p>1186 Pelham #3</p>
      <p>Dallas, TX 75209</p>
    </div>

    <div class="side-band side-band-left" role="img" aria-label="Decorative brand graphic area at the lower left edge"></div>
    <div class="side-band side-band-right" role="img" aria-label="Decorative brand graphic area along the right edge"></div>
  </section>

  <section class="sheet back-cover">
    <div class="cover-mark">
      <span class="cover-mark-square"></span>
      <span class="cover-mark-name">DRAVESCO MINING</span>
    </div>
  </section>
</body>
</html>
```